I need the following
2 versions (CMYK and RGB)
Full Page ad design 7.5" wide x 10" tall
No less than 300 dpi for print and 72dpi for web:
Full Color CMYK for print and RGB for web
Provide a high quality JPEG of the ad as well.

You can use the attached post card as a guide and use the info within it. You can get more information from our website at HaulingCrewFolks.net.
Also add a block with the following ... We work with real estate agents to make moving stress - free for their clients:
*Old Fashioned Customer Service
*Discounted rates
*Always Free Estimates
*Fully Licensed and Insured
*Communication From Start To Finish
*Full Service Moving

```html
<!DOCTYPE html>
<html lang="en">
<head>
<meta charset="utf-8">
<title>Hauling Crew Folks – Full Page Ad</title>
<link href="https://fonts.googleapis.com/css2?family=Poppins:ital,wght@0,400;0,500;0,600;0,700;0,800;1,400;1,500&family=Kaushan+Script&display=swap" rel="stylesheet">
<style>
:root{
  --orange:#f0a24a;
  --orange-deep:#ee8f2f;
  --orange-soft:#f2b46e;
  --charcoal:#3b3b3b;
  --charcoal-deep:#2f2f2f;
  --coupon:#4b4b4b;
  --ink:#2b2b2b;
  --paper:#ffffff;
  --page-bg:#ffffff;
  --star:#f7c22e;
}
*{margin:0;padding:0;box-sizing:border-box}
html,body{width:1200px;height:2778px;overflow:hidden;background:var(--page-bg)}
body{font-family:'Poppins',sans-serif;color:var(--ink);position:relative}
.ad{position:absolute;left:60px;top:669px;width:1080px;height:1440px;background:var(--paper);overflow:hidden;box-shadow:0 6px 18px rgba(0,0,0,.25)}
.abs{position:absolute}

/* hero */
.hero-photo{position:absolute;left:0;top:0;width:1080px;height:507px}
.brand{left:74px;top:82px;width:380px;text-align:center;font-weight:600;font-size:40px;line-height:1;color:var(--orange);letter-spacing:.5px}
.headline{left:70px;top:178px;font-weight:800;font-size:84px;line-height:1;color:var(--orange)}
.script-band{left:0;top:275px;width:560px;height:80px;background:var(--charcoal)}
.script{left:72px;top:280px;font-family:'Kaushan Script',cursive;font-size:54px;line-height:1.2;color:#fff;white-space:nowrap}
.stress{left:70px;top:360px;font-weight:800;font-size:70px;line-height:1;color:var(--charcoal-deep);letter-spacing:-1px}
.license{left:74px;top:446px;height:42px;display:flex;font-size:28px;line-height:42px}
.license .label{background:var(--orange-deep);color:#fff;padding:0 10px}
.license .number{background:var(--charcoal);color:#fff;padding:0 14px}

/* review */
.review-band{left:0;top:507px;width:1080px;height:267px;background:var(--charcoal)}
.review{left:140px;top:532px;width:880px;color:#fff;font-size:21px;line-height:24px;font-weight:500}
.review .stars{color:var(--star);letter-spacing:2px;font-size:22px}
.review .author{font-style:italic;display:block}

/* coupons */
.coupon{top:716px;width:279px;height:260px;background:var(--coupon);border-radius:4px;box-shadow:0 3px 6px rgba(0,0,0,.3);text-align:center;color:#fff}
.coupon::before{content:"";position:absolute;inset:7px;border:3px dashed #f0f0f0}
.coupon .amount{margin-top:38px;font-weight:800;font-size:54px;line-height:1}
.coupon .amount sup{font-size:26px;vertical-align:22px;margin-right:2px}
.coupon .range{margin-top:6px;font-weight:800;font-size:30px;line-height:1.15}
.coupon .price{font-weight:800;font-size:30px;line-height:1.3;color:var(--orange)}
.coupon .fine{margin-top:22px;font-style:italic;font-size:13px;color:#e6e6e6}

/* features */
.features{left:0;top:1002px;width:1080px;height:206px;background:var(--orange-soft)}
.divider{top:1006px;height:198px;border-left:2px dotted #6b5536}
.feature{display:flex;align-items:center;gap:20px}
.feature .icon{width:68px;height:68px;background:var(--charcoal);flex:none;display:flex;align-items:center;justify-content:center}
.feature .icon svg{width:42px;height:42px}
.feature .label{font-weight:700;font-size:20px;line-height:24px;color:var(--charcoal-deep);text-transform:uppercase}

/* benefits */
.benefits{top:1224px;font-size:21px;line-height:25px;color:var(--ink)}
.benefits li{list-style:none;position:relative;padding-left:28px;margin-bottom:7px}
.benefits li::before{content:"";position:absolute;left:0;top:6px;width:11px;height:11px;border-radius:50%;border:3px solid var(--orange);background:#fff}

/* footer */
.footer-bar{left:0;top:1337px;width:1080px;height:103px}
.phone{left:72px;top:1356px;display:flex;align-items:center;gap:14px;color:#fff;font-weight:700;font-size:58px;line-height:1.1}
.phone svg{width:30px;height:30px}
.contact{left:580px;font-weight:600;font-size:21px;line-height:1;color:var(--charcoal-deep);display:flex;align-items:center;gap:12px}
.contact svg{width:24px;height:24px}
</style>
</head>
<body>
<main class="ad">

  <svg class="hero-photo" viewBox="0 0 1080 507" aria-hidden="false">
    <defs>
      <linearGradient id="roomTone" x1="0" y1="0" x2="1" y2="1">
        <stop offset="0" stop-color="#6b5a4a"/>
        <stop offset=".5" stop-color="#8d7a66"/>
        <stop offset="1" stop-color="#cfc8c2"/>
      </linearGradient>
    </defs>
    <polygon points="447,0 1080,0 1080,507 592,507" fill="var(--orange)"/>
    <polygon role="img" aria-label="Photo of a living room mid-move with open cardboard boxes, furniture and a potted plant" points="463,0 1080,0 1080,507 612,507" fill="url(#roomTone)"/>
  </svg>

  <div class="abs brand">Hauling Crew Folks</div>
  <h1 class="abs headline">MOVING?</h1>
  <div class="abs script-band"></div>
  <p class="abs script">We'll make your move</p>
  <p class="abs stress">STRESS-FREE!</p>
  <div class="abs license"><span class="label">TXDMV:</span><span class="number">004812956B</span></div>

  <section class="abs review-band"></section>
  <blockquote class="abs review">
    <span class="stars">★★★★★</span> “Best movers in Dallas! They were fast, efficient, on time and very reasonably priced. They took so much care with our belongings. We have moved about 15 times and they are the best movers we have ever had. Highly recommend to anyone looking for movers. We really appreciate the care that they handled our furniture with. We will definitely be using them again. Thank you Ray and team!
    <span class="author">-Dana Whitfield</span>
  </blockquote>

  <div class="abs coupon" style="left:108px">
    <div class="amount"><sup>$</sup>25 OFF</div>
    <div class="range">MOVES UNDER</div>
    <div class="price">$500</div>
    <div class="fine">With this card. Call for details.</div>
  </div>
  <div class="abs coupon" style="left:402px">
    <div class="amount"><sup>$</sup>50 OFF</div>
    <div class="range">MOVES OVER</div>
    <div class="price">$500</div>
    <div class="fine">With this card. Call for details.</div>
  </div>
  <div class="abs coupon" style="left:699px">
    <div class="amount"><sup>$</sup>100 OFF</div>
    <div class="range">MOVES OVER</div>
    <div class="price">$1500</div>
    <div class="fine">With this card. Call for details.</div>
  </div>

  <section class="abs features"></section>
  <div class="abs divider" style="left:378px"></div>
  <div class="abs divider" style="left:758px"></div>

  <div class="abs feature" style="left:74px;top:1022px">
    <div class="icon"><svg viewBox="0 0 24 24" fill="none" stroke="#fff" stroke-width="1.5"><path d="M3 20h18M6 20v-6h12v6M9 14V9h6v5"/><circle cx="12" cy="6" r="2"/></svg></div>
    <div class="label">Old Fashioned<br>Customer Service</div>
  </div>
  <div class="abs feature" style="left:74px;top:1106px">
    <div class="icon"><svg viewBox="0 0 24 24" fill="none" stroke="#fff" stroke-width="1.5"><path d="M12 3l7 3v5c0 5-3 8-7 10-4-2-7-5-7-10V6z"/><path d="M9 12l2 2 4-4"/></svg></div>
    <div class="label">Fully Licensed<br>and Insured</div>
  </div>
  <div class="abs feature" style="left:412px;top:1022px">
    <div class="icon"><svg viewBox="0 0 24 24" fill="none" stroke="#fff" stroke-width="1.5"><path d="M4 20h16M6 20v-5M10 20v-8M14 20v-6M18 20v-10"/><circle cx="9" cy="6" r="3"/></svg></div>
    <div class="label">Discounted<br>Rates</div>
  </div>
  <div class="abs feature" style="left:412px;top:1106px">
    <div class="icon"><svg viewBox="0 0 24 24" fill="none" stroke="#fff" stroke-width="1.5"><rect x="3" y="4" width="10" height="7" rx="1"/><rect x="11" y="13" width="10" height="7" rx="1"/><path d="M5 14v4h3M19 5v5h-3"/></svg></div>
    <div class="label">Communication<br>From Start to Finish</div>
  </div>
  <div class="abs feature" style="left:790px;top:1022px">
    <div class="icon"><svg viewBox="0 0 24 24" fill="none" stroke="#fff" stroke-width="1.5"><rect x="5" y="3" width="14" height="18" rx="1"/><path d="M8 8h8M8 12h2M12 12h2M8 16h2M12 16h2"/></svg></div>
    <div class="label">Always Free<br>Estimates</div>
  </div>
  <div class="abs feature" style="left:790px;top:1106px">
    <div class="icon"><svg viewBox="0 0 24 24" fill="none" stroke="#fff" stroke-width="1.5"><rect x="8" y="9" width="8" height="7"/><path d="M4 20l4-4M20 20l-4-4M4 5h4M16 5h4"/></svg></div>
    <div class="label">Full Service<br>Moving</div>
  </div>

  <ul class="abs benefits" style="left:74px">
    <li>Save time and effort with packing services</li>
    <li>Keep your belongings safe with<br>reputable movers</li>
  </ul>
  <ul class="abs benefits" style="left:548px">
    <li>Save money with our cost-effective pricing</li>
    <li>Fully licensed and insured</li>
  </ul>

  <svg class="abs footer-bar" viewBox="0 0 1080 103" aria-hidden="true">
    <polygon points="0,0 545,0 570,103 0,103" fill="var(--charcoal)"/>
  </svg>
  <div class="abs phone">
    <svg viewBox="0 0 24 24" fill="var(--orange)"><path d="M6.6 10.8a15 15 0 006.6 6.6l2.2-2.2a1 1 0 011-.25 11.4 11.4 0 003.6.57 1 1 0 011 1V20a1 1 0 01-1 1A17 17 0 013 4a1 1 0 011-1h3.5a1 1 0 011 1c0 1.25.2 2.45.57 3.6a1 1 0 01-.25 1z"/></svg>
    <span>(555) 014-2297</span>
  </div>
  <div class="abs contact" style="top:1354px">
    <svg viewBox="0 0 24 24" fill="none" stroke="var(--charcoal-deep)" stroke-width="2"><rect x="3" y="6" width="18" height="13" rx="1"/><path d="M3 7l9 6 9-6"/></svg>
    <span>hello@haulingcrewfolks.net</span>
  </div>
  <div class="abs contact" style="top:1392px">
    <svg viewBox="0 0 24 24" fill="none" stroke="var(--charcoal-deep)" stroke-width="2"><circle cx="12" cy="12" r="9"/><path d="M3 12h18M12 3c3 3 3 15 0 18M12 3c-3 3-3 15 0 18"/></svg>
    <span>HaulingCrewFolks.net</span>
  </div>

</main>
</body>
</html>
```